DJ Marcus Tevane

I'm looking for a professional but still artsy/progressive design. I come from a hip hop/club DJ background playing a lot of underground music but have switched to doing more corporate parties and weddings recently. I am all about keeping the dancefloor moving and emotionally connecting with the crowd. I'd like a trendy/updated color palette. Something that's clean enough that looks professional but also trendy enough to convey that by the end of the night we'll be sweatily dancing to the latest hits. Some designers/artists I like: Rolo Pemberack, Gavin Struthe, Dorian Fellick, Orbitex 3100, Wade Ipsley.

```html
<!DOCTYPE html>
<html lang="en">
<head>
<meta charset="utf-8">
<title>DJ Marcus Tevane — Business Card</title>
<link href="https://fonts.googleapis.com/css2?family=Oswald:wght@500;600&family=Lato:wght@400;700&display=swap" rel="stylesheet">
<style>
  :root {
    --stage: #3a3b3d;
    --ink: #0b0b0b;
    --paper: #ffffff;
    --accent: #ec7a1c;
    --text: #1c1c1c;
    --rule: #d9dee2;
  }
  * { box-sizing: border-box; margin: 0; padding: 0; }
  html, body { width: 1200px; height: 1200px; overflow: hidden; }
  body {
    background: var(--stage);
    display: flex;
    flex-direction: column;
    align-items: center;
    justify-content: center;
    gap: 56px;
  }
  .card {
    width: 860px;
    height: 492px;
    position: relative;
    box-shadow: 0 14px 30px rgba(0,0,0,.35);
  }
  .card--front {
    background: var(--ink);
    border-radius: 84px 0 84px 0;
    display: flex;
    align-items: center;
    justify-content: center;
  }
  .card--back {
    background: var(--paper);
    border-radius: 0 84px 0 84px;
    display: flex;
    align-items: center;
  }
  .wordmark {
    display: flex;
    align-items: center;
    gap: 22px;
    font-family: "Oswald", sans-serif;
    font-weight: 600;
    text-transform: uppercase;
    letter-spacing: .5px;
    line-height: 1;
  }
  .wordmark__dot {
    border-radius: 50%;
    background: var(--accent);
    flex: none;
  }
  .card--front .wordmark { color: var(--paper); font-size: 78px; }
  .card--front .wordmark__dot { width: 54px; height: 54px; }
  .brand-panel {
    width: 430px;
    height: 100%;
    display: flex;
    align-items: center;
    justify-content: center;
  }
  .card--back .wordmark { color: var(--ink); font-size: 44px; gap: 14px; flex-direction: column; text-align: center; }
  .card--back .wordmark__dot { width: 34px; height: 34px; }
  .divider {
    width: 1px;
    height: 220px;
    background: var(--rule);
  }
  .contact {
    padding-left: 44px;
    font-family: "Lato", sans-serif;
    color: var(--text);
  }
  .contact__name {
    font-family: "Oswald", sans-serif;
    font-weight: 500;
    font-size: 34px;
    color: var(--accent);
    text-transform: uppercase;
    line-height: 1;
  }
  .contact__role { font-size: 20px; margin: 4px 0 12px; }
  .contact__list { list-style: none; }
  .contact__item {
    display: flex;
    align-items: center;
    gap: 10px;
    font-size: 21px;
    line-height: 1.3;
  }
  .contact__item svg { width: 16px; height: 16px; fill: var(--accent); flex: none; }
  .contact__address { font-size: 21px; line-height: 1.3; margin-top: 10px; }
</style>
</head>
<body>
  <section class="card card--front">
    <div class="wordmark"><span class="wordmark__dot"></span>DJ Marcus Tevane</div>
  </section>

  <section class="card card--back">
    <div class="brand-panel">
      <div class="wordmark"><span class="wordmark__dot"></span>DJ Marcus Tevane</div>
    </div>
    <div class="divider"></div>
    <div class="contact">
      <p class="contact__name">Leona Gratwick</p>
      <p class="contact__role">Managing Director</p>
      <ul class="contact__list">
        <li class="contact__item">
          <svg viewBox="0 0 16 16"><path d="M3 1h3l1.5 4-2 1.2a9 9 0 0 0 4.3 4.3L11 8.5l4 1.5v3a2 2 0 0 1-2 2A13 13 0 0 1 1 3a2 2 0 0 1 2-2z"/></svg>
          044-555 018 274
        </li>
        <li class="contact__item">
          <svg viewBox="0 0 16 16"><path d="M4 0h8a1 1 0 0 1 1 1v14a1 1 0 0 1-1 1H4a1 1 0 0 1-1-1V1a1 1 0 0 1 1-1zm1 2v10h6V2zm3 11a1 1 0 1 0 0 2 1 1 0 0 0 0-2z"/></svg>
          044-555 018 274
        </li>
        <li class="contact__item">
          <svg viewBox="0 0 16 16"><path d="M0 3h16v10H0zm1.5 1.5L8 9l6.5-4.5V4h-13z"/></svg>
          hello@tevanemix.com
        </li>
        <li class="contact__item">
          <svg viewBox="0 0 16 16"><circle cx="8" cy="8" r="8"/></svg>
          www.tevanemix.com
        </li>
      </ul>
      <p class="contact__address">48 Harrowgate Lane<br>Northfield, 204517.</p>
    </div>
  </section>
</body>
</html>
```